Pagecraft Design for Fruit & Veggie Swap Site

I need a pagecraft design for the HOME PAGE of a company located in Kona, Hawaii called Leafway Exchange Hawaii. Leafway Exchange Hawaii (LEH) is a site intended to support the local food movement by connecting neighbors in order for them to swap/trade produce from their farm or garden. The purpose of this site is to support sustainable agriculture in Hawaii and encourage community interaction.

The model of the site is similar to:
http://www.harvtrade.me/ (I really like the simple design of this site)
http://www.plotbarter.co.uk/ (I don't like the design of this site, just the functionality. The design is too busy and unbalanced.)
Unlike the two sites listed above, however, LEH is only targeted at people living on the Big Island of Hawaii.

The site is simply intended to be a platform to connect people, then they are free to swap or barter off site, similar to the way postboardly connects people. Users can create "posts" for crops that they have available for swap, which are searchable based on name and location.

I have created a very basic, no-css, dev version of the site to work on the back end, which is located here: http://leafwayexchangehawaii.com/test
Feel free to register and create a test post to get a feel for how it works.

The images I have uploaded are just for ideas and do not have to be in the design.

Target Market(s)

The targeted audience is gardeners and farmers on the Big Island of Hawaii. These people are quite varied in age and technical ability.

Industry/Entity Type

Agriculture

Requirements
Must have
• On the homepage, I would like to have a list of the most recent "posts", displayed as the post title, with the most recent post at the top of the list. In the test site, this is located in the right column, but it doesn't have to be in that location in the final design.

I would also like the option to "Add new listing" to be displayed creatively on the home page. This can be in the form of a graphic that links to a form on another page.

I would also like to have a search box on the homepage. Users can search by crop name and/or location.

The main focal point of the home page will be a Mapsly map application of the Big Island. I am in the process of developing this. You can see the map on the test site, please keep in mind that this map may change slightly in future revisions. Feel free to change the size and styling of the map to fit your design.

I would like the homepage to have a simple and clean layout, making it clear to users how the site works.
For the graphics, I would like to incorporate the "crop circles" idea (yes, like the alien crop circles in fields) with fruits and veggies (including tropical fruit found in Hawaii like banana, coconut, lychee, taro, oranges, as well as traditional vegetables like carrots, lettuce, etc.), and also potentially with the idea of sharing and circulating produce with neighbors.
Please note that those specific fruits and veggies don't need to be used, or that many of them, I was just giving them as examples.

I would also like to have a place on the homepage where users can login/sign up. This can be a login form with a sign up link, or a login link and a sign up link.

I would like the entire design to fit on a page without having to scroll.

Once the site has a substantial user base, I plan to incorporate advertising. Please create a design that will be easy to integrate ads into in the future, most likely in the side bar or footer. I do not want the original design to have ad space, just the ability to add it easily in the future and having it look good with the current design.

```html
<!DOCTYPE html>
<html lang="en">
<head>
<meta charset="utf-8">
<title>Leafway Exchange Hawaii</title>
<link href="https://fonts.googleapis.com/css2?family=Bubblegum+Sans&family=Open+Sans:wght@400;600&family=Roboto:wght@400;500;700&family=Roboto+Condensed:wght@700&display=swap" rel="stylesheet">
<style>
:root{
  --field-dark:#5f7d2c;
  --field-mid:#8aa04a;
  --field-light:#b8c585;
  --orange:#ee7a12;
  --orange-light:#f6a03a;
  --green-text:#6a8d1f;
  --green-btn:#7fbf2a;
  --text:#555;
  --dark:#333;
  --nav-text:#3a3a3a;
  --footer:#2f3d1c;
  --line:#e3e3e3;
  --white:#fff;
  --map-sea:#a9c0e3;
  --map-land:#f0ede5;
  --map-park:#c3dca3;
}
*{box-sizing:border-box;margin:0;padding:0}
html,body{width:1200px;height:1018px;overflow:hidden}
body{position:relative;background:var(--white);font-family:"Open Sans",sans-serif;color:var(--text)}
a{text-decoration:none}
.field{position:absolute;left:0;top:0;width:1200px;height:580px;
  background:linear-gradient(180deg,var(--field-dark) 0%,var(--field-mid) 45%,var(--field-light) 70%,rgba(255,255,255,0) 100%)}
.fruit{position:absolute;border-radius:40%}
.fruit-left{left:0;top:140px;width:196px;height:320px;
  background:radial-gradient(circle at 40% 35%,#c7d35a 0 22%,transparent 40%),radial-gradient(circle at 45% 70%,#7a3d5c 0 18%,transparent 35%),radial-gradient(circle at 70% 85%,#f2a21b 0 15%,transparent 30%),radial-gradient(circle at 20% 95%,#f4d23b 0 14%,transparent 30%)}
.fruit-right{left:1008px;top:0;width:192px;height:460px;
  background:radial-gradient(circle at 50% 12%,#c62828 0 16%,transparent 30%),radial-gradient(circle at 40% 45%,#d23b2a 0 14%,transparent 28%),radial-gradient(circle at 55% 65%,#f5c928 0 15%,transparent 30%),radial-gradient(circle at 45% 80%,#f07a17 0 15%,transparent 30%),radial-gradient(circle at 80% 78%,#8dc03b 0 14%,transparent 28%)}
.fruit-top{left:490px;top:58px;width:230px;height:51px;border-radius:30px 30px 0 0;
  background:linear-gradient(90deg,#6e8b2a,#c9302c,#f2b120,#e58a1a,#7c9b2b)}
.logo{position:absolute;left:194px;top:28px;display:flex;align-items:center;gap:10px}
.logo-mark{width:62px;height:62px;border-radius:50%;background:#f3edc2}
.logo-name{font-family:"Roboto",sans-serif;font-weight:700;font-size:21px;line-height:24px;color:var(--white)}
.login{position:absolute;left:726px;top:14px;width:284px;font-family:"Roboto",sans-serif;font-size:11.5px;color:var(--white)}
.login-fields{display:flex;gap:9px}
.login-fields span{display:block;width:137px;height:23px;background:#e8e8e8;color:#666;font-style:italic;font-size:12px;padding:4px 7px;border:1px solid #cfcfcf}
.login-options{display:flex;gap:16px;margin-top:14px}
.login-options span{display:flex;align-items:center;gap:6px}
.check{width:10px;height:10px;background:var(--white);position:relative}
.check::after{content:"";position:absolute;left:2px;top:1px;width:4px;height:6px;border:solid #333;border-width:0 2px 2px 0;transform:rotate(45deg)}
.login-actions{display:flex;align-items:center;gap:14px;margin-top:7px}
.btn-signin{width:79px;height:24px;background:var(--green-btn);color:#fff;font-weight:500;font-size:13px;text-align:center;line-height:24px;border:1px solid #a8dc5a}
.login-actions a{color:var(--white);font-size:12px;text-decoration:underline}
.nav{position:absolute;left:192px;top:109px;width:817px;height:42px;background:var(--white);border-radius:6px;box-shadow:0 1px 3px rgba(0,0,0,.25);display:flex;align-items:center;padding-left:12px;font-family:"Roboto",sans-serif;font-weight:500;font-size:14px}
.nav a{color:var(--nav-text);margin-right:30px}
.nav a.active{background:var(--orange);color:#fff;padding:3px 14px;border-radius:14px;margin-right:18px}
.search{position:absolute;right:12px;top:9px;width:190px;height:24px;border:1px solid #ccc;border-radius:12px;font-size:12px;font-style:italic;font-weight:400;color:#666;padding:4px 12px}
.search-btn{position:absolute;right:-1px;top:-1px;width:24px;height:24px;border-radius:50%;background:var(--orange);display:flex;align-items:center;justify-content:center}
.map-frame{position:absolute;left:192px;top:160px;width:817px;height:290px;background:var(--white);border-radius:5px;box-shadow:0 1px 4px rgba(0,0,0,.25);padding:8px 7px}
.map{width:802px;height:274px;background:linear-gradient(100deg,var(--map-sea) 0 8%,var(--map-land) 20%,var(--map-park) 55%,var(--map-land) 80%,var(--map-sea) 96%)}
.welcome{position:absolute;left:192px;top:476px;width:555px}
.welcome h1{font-family:"Bubblegum Sans",cursive;font-weight:400;font-size:30px;color:#444;line-height:40px}
.welcome h1 span{color:var(--orange)}
.welcome p{font-size:12.3px;line-height:18.4px;margin-top:2px}
.welcome p + p{margin-top:18px}
.read-more{position:absolute;left:194px;top:889px;width:84px;height:22px;border-radius:11px;background:#fff;box-shadow:0 1px 3px rgba(0,0,0,.3);font-size:10.5px;color:var(--orange);display:flex;align-items:center;justify-content:center;gap:4px}
.recent{position:absolute;left:775px;top:485px;width:234px}
.recent h2{position:relative;height:36px;background:linear-gradient(var(--orange-light),var(--orange));font-family:"Bubblegum Sans",cursive;font-weight:400;font-size:23px;color:#fff;padding:2px 14px;border-radius:3px}
.recent h2::after{content:"";position:absolute;left:34px;bottom:-8px;border:8px solid transparent;border-bottom:0;border-top-color:var(--orange)}
.recent ul{list-style:none;margin-top:9px}
.recent li{height:26.7px;border-bottom:1px solid var(--line);font-size:12.8px;color:#333;padding:1px 0 0 14px;position:relative;line-height:24px}
.recent li::before{content:"»";position:absolute;left:0;color:#999}
.recent li span{color:var(--green-text)}
.view-all{margin-top:13px;height:24px;background:#ececec;font-size:11.5px;color:var(--green-text);padding:4px 15px}
.cta{position:absolute;left:278px;top:930px;width:634px;height:54px;border-radius:27px;background:linear-gradient(#666,#333);border:3px solid #fff;box-shadow:0 1px 4px rgba(0,0,0,.4);overflow:hidden;z-index:2;font-family:"Roboto Condensed",sans-serif;font-weight:700}
.cta-question{position:absolute;left:37px;top:6px;color:#fff;font-size:28px;font-family:"Roboto",sans-serif;font-weight:500}
.cta-button{position:absolute;left:394px;top:0;width:240px;height:48px;border-radius:24px;background:linear-gradient(var(--orange-light),var(--orange));color:#fff;font-size:23px;display:flex;align-items:center;padding-left:25px;gap:14px}
.footer{position:absolute;left:0;top:956px;width:1200px;height:62px;background:var(--footer);color:#e8e8e8;font-size:12px;text-align:center;padding-top:36px}
</style>
</head>
<body>
<div class="field" role="img" aria-label="Aerial photo of a green crop field with circle patterns"></div>
<div class="fruit fruit-left" role="img" aria-label="Photo of grapes, orange, banana and kiwi"></div>
<div class="fruit fruit-right" role="img" aria-label="Photo of cherries, apples, bananas, oranges and kiwi"></div>
<div class="fruit fruit-top" role="img" aria-label="Photo of assorted vegetables and tropical fruit"></div>

<header>
  <div class="logo"><span class="logo-mark"></span><span class="logo-name">Leafway Exchange<br>Hawaii</span></div>
  <form class="login">
    <div class="login-fields"><span>Your email</span><span>Password</span></div>
    <div class="login-options"><span><i class="check"></i>Forgot your password?</span><span><i class="check"></i>Create New Account</span></div>
    <div class="login-actions"><span class="btn-signin">SIGN IN</span><span>or&nbsp; <a href="#">Sign Up</a></span></div>
  </form>
</header>

<nav class="nav">
  <a class="active" href="#">HOME</a><a href="#">ABOUT US</a><a href="#">BLOG</a><a href="#">FORUM</a><a href="#">GARDERN SHOP</a><a href="#">CONTACT US</a>
  <div class="search">Enter crop name
    <span class="search-btn"><svg width="12" height="12" viewBox="0 0 12 12"><circle cx="5" cy="5" r="3.5" fill="none" stroke="#fff" stroke-width="1.6"/><line x1="7.6" y1="7.6" x2="11" y2="11" stroke="#fff" stroke-width="1.8"/></svg></span>
  </div>
</nav>

<section class="map-frame">
  <div class="map" role="img" aria-label="Interactive map of the Big Island of Hawaii with red pins marking crop posts"></div>
</section>

<main class="welcome">
  <h1>Welcome to <span>Leafway Exchange Hawaii</span></h1>
  <p>Lorem Ipsum is simply dummy text of the printing and typesetting industry. Lorem Ipsum has been the industry's standard dummy text ever since the 1500s, when an unknown printer took a galley of type and scrambled it to make a type specimen book. It has survived not only five centuries, but also the leap into electronic typesetting, remaining essentially unchanged. It was popularised in the 1960s with the release of Typesheet sheets containing Lorem Ipsum passages, and more recently with desktop publishing software like Folio LayoutKit, you need to be sure there isn't anything embarrassing hidden in the middle of text</p>
  <p>It is a long established fact that a reader will be distracted by the readable content of a page when looking at its layout. The point of using Lorem Ipsum is that it has a more-or-less normal distribution of letters, there are many variations of passages of lorem ipsum available, but the majority have suffered alteration in some form, by injected humour, or randomised words which don't look even slightly believable. If you are going to use a passage of lorem ipsum, you need to be sure there isn't anything embarrassing hidden in the middle of text. All the lorem ipsum generators on the Internet tend to repeat predefined chunks as necessary, making this the first true generator on the Internet. It uses a dictionary of over 200 Latin words, combined with a handful of model sentence structures, to generate Lorem Ipsum which looks reasonable. The generated Lorem Ipsum is therefore always free from repetition, injected humour, or non-characteristic words etc</p>
</main>
<a class="read-more" href="#">Read More <svg width="9" height="9" viewBox="0 0 9 9"><circle cx="4.5" cy="4.5" r="3.8" fill="none" stroke="#ee7a12"/><path d="M3.8 2.8 5.5 4.5 3.8 6.2" fill="none" stroke="#ee7a12"/></svg></a>

<aside class="recent">
  <h2>Recent Post</h2>
  <ul>
    <li>Coconut <span>(Hilo)</span></li>
    <li>Mango <span>(Pahoa)</span></li>
    <li>Coffee cherries <span>(Kapoho)</span></li>
    <li>Lemons <span>(Pahala)</span></li>
    <li>Oranges <span>(Kohala)</span></li>
    <li>Lettuce <span>(Holualoa)</span></li>
    <li>Testing redirect <span>(Volcano)</span></li>
    <li>Testing redirect2 <span>(Honaunau)</span></li>
    <li>Testing redirect3 <span>(Honaunau)</span></li>
    <li>Testing redirect <span>(Honokaa)</span></li>
    <li>Coconut <span>(Hilo)</span></li>
    <li>Mango <span>(Pahoa)</span></li>
    <li>Coffee cherries <span>(Kapoho)</span></li>
  </ul>
  <div class="view-all">View All ›</div>
</aside>

<a class="cta" href="#">
  <span class="cta-question">How Something to share?</span>
  <span class="cta-button">ADD NEW LISTING <svg width="10" height="16" viewBox="0 0 10 16"><path d="M2 2 8 8 2 14" fill="none" stroke="#fff" stroke-width="2.4"/></svg></span>
</a>

<footer class="footer">Copyright © 2013 Leafway Exchange Hawaii.&nbsp; All Rights Reserved.</footer>
</body>
</html>
```